A new type of air filter for interior of vehicles

HI
I have included a file to show the basics of what i want and all the information that should be needed ,i now need this to be "designed" and to be created for a information flyer first and as things progress web pages etc etc look forward to the designs

Industry/Entity Type

Interior

Contact Information for Business Card

probably the same "theme type" as the brochure which will carry through to Business card and on to online marketing in the future

Font styles to use
Serif
Sans Serif

```html
<!DOCTYPE html>
<html lang="en">
<head>
<meta charset="utf-8">
<title>Cabin Breeze Filters Co — Business Cards</title>
<link rel="stylesheet" href="https://fonts.googleapis.com/css2?family=Josefin+Slab:wght@600&display=swap">
<style>
  :root {
    --page: #000000;
    --sky: #41a8f3;
    --paper: #ffffff;
    --slate: #808080;
    --ink: #000000;
  }
  html, body {
    margin: 0;
    padding: 0;
    width: 1200px;
    height: 1105px;
    overflow: hidden;
    background: var(--page);
  }
  .sheet {
    position: relative;
    width: 1200px;
    height: 1105px;
    font-family: "Josefin Slab", Georgia, serif;
    font-weight: 600;
  }
  .card {
    position: absolute;
    width: 545px;
    box-sizing: border-box;
  }
  .card--front { left: 39px; }
  .card--back { left: 614px; }
  .row-1 { top: 43px; height: 313px; }
  .row-2 { top: 378px; height: 310px; }
  .row-3 { top: 725px; height: 311px; }
  .tone-sky { background: var(--sky); }
  .tone-paper { background: var(--paper); }
  .tone-slate { background: var(--slate); }

  .brand {
    position: absolute;
    inset: 0;
    display: flex;
    align-items: center;
    justify-content: center;
    gap: 14px;
    color: var(--paper);
    font-size: 30px;
    letter-spacing: 0.5px;
  }
  .brand-dot {
    width: 26px;
    height: 26px;
    border-radius: 50%;
    background: var(--paper);
    flex: none;
  }

  .details {
    position: absolute;
    left: 24px;
    top: 113px;
    padding-left: 10px;
    border-left: 2px solid var(--ink);
    color: var(--ink);
  }
  .company {
    margin: 0 0 4px;
    font-size: 28px;
    font-weight: 600;
    line-height: 34px;
  }
  .contact-list {
    margin: 0;
    padding: 0;
    list-style: none;
    font-size: 13px;
    line-height: 16px;
  }

  .details--icons {
    left: 38px;
    top: 92px;
    padding-left: 0;
    border-left: none;
    color: var(--paper);
  }
  .details--icons .company { margin-bottom: 6px; }
  .details--icons .contact-list {
    font-size: 15px;
    line-height: 17px;
  }
  .details--icons li {
    display: flex;
    align-items: center;
    gap: 7px;
  }
  .line-icon { flex: none; }
</style>
</head>
<body>
<main class="sheet">

  <section class="card card--front row-1 tone-sky">
    <div class="brand"><span class="brand-dot"></span>Cabin Breeze Filters Co</div>
  </section>
  <section class="card card--back row-1 tone-paper">
    <div class="details">
      <h2 class="company">Cabin Breeze Filters Co</h2>
      <ul class="contact-list">
        <li>0400 318 926</li>
        <li>hello@cabinbreeze.net</li>
        <li>CabinBreezeFilters.com.au</li>
        <li>Po Box 17</li>
        <li>Harbour Bend Qld</li>
        <li>4299</li>
      </ul>
    </div>
  </section>

  <section class="card card--front row-2 tone-sky">
    <div class="brand"><span class="brand-dot"></span>Cabin Breeze Filters Co</div>
  </section>
  <section class="card card--back row-2 tone-sky">
    <div class="details details--icons">
      <h2 class="company">Cabin Breeze Filters Co</h2>
      <ul class="contact-list">
        <li><svg class="line-icon" width="11" height="11" viewBox="0 0 11 11"><rect x="0" y="6" width="3" height="5" fill="#fff"/><rect x="4" y="3" width="3" height="8" fill="#fff"/><rect x="8" y="0" width="3" height="11" fill="#fff"/></svg>0400 318 926</li>
        <li><svg class="line-icon" width="11" height="11" viewBox="0 0 11 11"><rect x="0" y="6" width="3" height="5" fill="#fff"/><rect x="4" y="3" width="3" height="8" fill="#fff"/><rect x="8" y="0" width="3" height="11" fill="#fff"/></svg>hello@cabinbreeze.net</li>
        <li><svg class="line-icon" width="11" height="11" viewBox="0 0 11 11"><rect x="0" y="6" width="3" height="5" fill="#fff"/><rect x="4" y="3" width="3" height="8" fill="#fff"/><rect x="8" y="0" width="3" height="11" fill="#fff"/></svg>CabinBreezeFilters.com.au</li>
        <li><svg class="line-icon" width="11" height="11" viewBox="0 0 11 11"><rect x="0" y="6" width="3" height="5" fill="#fff"/><rect x="4" y="3" width="3" height="8" fill="#fff"/><rect x="8" y="0" width="3" height="11" fill="#fff"/></svg>Po Box 17</li>
        <li><svg class="line-icon" width="11" height="11" viewBox="0 0 11 11"><rect x="0" y="6" width="3" height="5" fill="#fff"/><rect x="4" y="3" width="3" height="8" fill="#fff"/><rect x="8" y="0" width="3" height="11" fill="#fff"/></svg>Harbour Bend Qld</li>
        <li><svg class="line-icon" width="11" height="11" viewBox="0 0 11 11"><rect x="0" y="6" width="3" height="5" fill="#fff"/><rect x="4" y="3" width="3" height="8" fill="#fff"/><rect x="8" y="0" width="3" height="11" fill="#fff"/></svg>4299</li>
      </ul>
    </div>
  </section>

  <section class="card card--front row-3 tone-slate">
    <div class="brand"><span class="brand-dot"></span>Cabin Breeze Filters Co</div>
  </section>
  <section class="card card--back row-3 tone-slate">
    <div class="details">
      <h2 class="company">Cabin Breeze Filters Co</h2>
      <ul class="contact-list">
        <li>0400 318 926</li>
        <li>hello@cabinbreeze.net</li>
        <li>CabinBreezeFilters.com.au</li>
        <li>Po Box 17</li>
        <li>Harbour Bend Qld</li>
        <li>4299</li>
      </ul>
    </div>
  </section>

</main>
</body>
</html>
```